PEACFUL ACUPUNCTURE PRACTITIONER NEEDS A NEW COAT

I need a new design for an exiting website http://stillwillowneedlework.example/ for a acupuncturist. This will be a minimalism design with lots and lots of white space. Home page and one interior page. Please keep the feeling of calm and peaceful serenity. For Color scheme: https://www.harborfernclinic.example/fertility. The bottom part of the home page with sections and links to the service pages: https://mossgatewellness.example/. The client likes this the best: http://qlhealing.example/. I'm attaching the logo and content pages.

Target Market(s)

Women

Industry/Entity Type

Wellness, health, wellbeing, meditation

Number of Pages Required

2 page

Font styles to use
Sans Serif
Decorative

Colors

Designer to choose colors to be used in the design.

Requirements
Must have
Nice to have
• Follow new website drafts and links
Should not have
• Busy with bright colors. No poping

```html
<!DOCTYPE html>
<html lang="en">
<head>
<meta charset="utf-8">
<title>Still Willow Acupuncture</title>
<link rel="stylesheet" href="https://fonts.googleapis.com/css2?family=Raleway:wght@400;500;600&display=swap">
<style>
  :root {
    --paper: #ffffff;
    --blush: #d8bcbd;
    --ink: #444444;
    --ink-dark: #111111;
    --rule: #cfcfcf;
    --dot: #4a4a4a;
    --icon: #cfcfcf;
    --petal-deep: #c49a9c;
    --petal-mid: #dcc2c4;
    --petal-pale: #eee3e5;
  }
  * { margin: 0; padding: 0; box-sizing: border-box; }
  html, body {
    width: 1200px; height: 778px; overflow: hidden;
    background: var(--blush);
    font-family: "Raleway", sans-serif;
    color: var(--ink);
  }
  .page {
    position: relative; width: 1200px; height: 737px;
    background: var(--paper);
    border-radius: 0 0 40px 40px / 0 0 54px 54px;
  }
  .contact { position: absolute; left: 79px; top: 38px; font-size: 13px; font-weight: 600; line-height: 18px; }
  .brand { position: absolute; left: 0; width: 1200px; top: 34px; text-align: center; color: #555; font-weight: 400; }
  .brand-name { display: block; font-size: 40px; line-height: 44px; letter-spacing: 1px; }
  .brand-sub { display: block; font-size: 25px; line-height: 26px; letter-spacing: 7px; }
  .shop { position: absolute; left: 1025px; top: 37px; font-size: 13px; font-weight: 600; }
  .social { position: absolute; top: 36px; width: 22px; height: 22px; border-radius: 50%; background: var(--icon); }
  .intro {
    position: absolute; left: 222px; width: 800px; top: 140px;
    text-align: center; font-size: 16.7px; line-height: 21px;
  }
  .flower {
    position: absolute; left: 405px; top: 283px; width: 388px; height: 386px;
    border-radius: 50%;
    background: radial-gradient(circle, var(--petal-deep) 0%, var(--petal-mid) 45%, var(--petal-pale) 75%, rgba(238,227,229,0) 100%);
  }
  .focus-map { position: absolute; left: 0; top: 0; }
  .focus-label { position: absolute; font-size: 12.5px; line-height: 16px; color: #555; text-transform: uppercase; }
  .nav { position: absolute; top: 712px; left: 0; width: 1200px; list-style: none; font-size: 14px; color: var(--ink-dark); }
  .nav li { position: absolute; white-space: nowrap; }
</style>
</head>
<body>
  <div class="page">
    <div class="contact">
      <div>hello@stillwillow.example</div>
      <div>+1 555 010 200</div>
    </div>

    <div class="brand">
      <span class="brand-name">Still Willow</span>
      <span class="brand-sub">ACUPUNCTURE</span>
    </div>

    <div class="shop">SHOP</div>
    <span class="social" style="left:1067px"></span>
    <span class="social" style="left:1096px"></span>
    <span class="social" style="left:1126px"></span>

    <p class="intro">Acupuncture &amp; Chinese Herbal Medicine are rooted in over 3000 years of history and tradition.<br>As a complete medical system that has remained flexible and relevant we honor what has worked<br>from the past while embracing the medicine of tomorrow.</p>

    <div class="flower" role="img" aria-label="Layered lotus flower mandala in soft rose tones"></div>

    <svg class="focus-map" width="1200" height="737" viewBox="0 0 1200 737" aria-hidden="true">
      <g stroke="var(--rule)" stroke-width="1">
        <line x1="372" y1="347" x2="600" y2="347"/>
        <line x1="287" y1="477" x2="467" y2="477"/>
        <line x1="733" y1="477" x2="947" y2="477"/>
        <line x1="600" y1="607" x2="844" y2="607"/>
      </g>
      <g fill="var(--dot)">
        <circle cx="372" cy="344" r="7.5"/>
        <circle cx="287" cy="477" r="2.6"/>
        <circle cx="947" cy="477" r="3.2"/>
        <circle cx="844" cy="607" r="6.5"/>
      </g>
    </svg>

    <div class="focus-label" style="left:385px; top:314px">Hormone<br>Balance</div>
    <div class="focus-label" style="left:295px; top:444px">Fertility &amp;<br>Pregnancy</div>
    <div class="focus-label" style="left:858px; top:445px">Emontional<br>Well&nbsp; Being</div>
    <div class="focus-label" style="left:761px; top:573px">Strenght &amp;<br>Structure</div>

    <ul class="nav">
      <li style="left:240px">HOME</li>
      <li style="left:398px">ABOUT US</li>
      <li style="left:558px">FOCUS AREAS</li>
      <li style="left:757px">TESTIMONIALS</li>
      <li style="left:948px; top:1px">CONTACT</li>
    </ul>
  </div>
</body>
</html>
```